Brochure Annual Report Design

I want to create a brochure / annual report for our company. Can you help me. I like this design. https://pixelstallhub.com/Brightfold/2847163-Annual-Report-2018. Here is our company website www.velmordental.com. Please take the logo from there. Our website needs an upgrade in how it looks. I would like the brochure annual report and the website to look somewhat congruent. I also want to create a very high end magazine that is fun for our company eventually.

We are a company that helps dentists create better practices by really improving the way they do business and motivating their teams. As a result they have more fun, more profit, happier team members, and they all have better lives.

Target Market(s)

dentist

Industry/Entity Type

Dental

Number of Pages Required

5+ page

Colors
0255a3
85cae6
ffffff

Requirements
Must have
• Must look really good.
Nice to have
• Any creative suggestions are welcomed. I need a website that looks congruent to the brochure and annual report. I also want to create a very high end magazine that is fun for our company eventually.
Should not have
• I don't like low quality design.

```html
<!DOCTYPE html>
<html lang="en">
<head>
<meta charset="utf-8">
<title>Velmor Dental – Our Secret Sauce</title>
<link href="https://fonts.googleapis.com/css2?family=Barlow:wght@400;500;600&family=Barlow+Semi+Condensed:wght@400;700&display=swap" rel="stylesheet">
<style>
  :root {
    --navy: #0255a3;
    --sky: #85cae6;
    --band: #72c7e8;
    --paper: #ffffff;
    --page-grey: #f1f2f3;
    --ink: #2b2b2b;
    --muted: #555;
    --stage: #ececec;
  }
  * { margin: 0; padding: 0; box-sizing: border-box; }
  html, body { width: 1200px; height: 900px; overflow: hidden; background: var(--stage); }
  body { font-family: "Barlow", sans-serif; color: var(--ink); }

  .spread {
    position: absolute; left: 40px; top: 40px;
    width: 1120px; height: 820px; display: flex;
    box-shadow: 0 6px 24px rgba(0,0,0,.12);
  }
  .page { position: relative; width: 560px; height: 820px; background: var(--page-grey); overflow: hidden; }

  .team-photo {
    position: absolute; top: 0; height: 238px;
    background: linear-gradient(180deg, #e9ecef 0%, #c9c3bd 45%, #4a4645 80%, #2c2b2c 100%);
  }
  .page--left .team-photo { left: 375px; width: 185px; }
  .page--right .team-photo { left: 0; width: 560px; }

  .brand {
    position: absolute; top: 22px;
    font-family: "Barlow", sans-serif; font-weight: 600; font-size: 22px;
    color: var(--navy); letter-spacing: .2px;
  }
  .page--left .brand { left: 75px; }
  .page--right .brand { right: 48px; color: var(--paper); }

  .section-title { position: absolute; left: 75px; top: 148px; font-family: "Barlow Semi Condensed", sans-serif; line-height: 1.15; }
  .section-title .kicker { display: block; font-weight: 700; font-size: 25px; color: var(--band); letter-spacing: .5px; }
  .section-title .sub { display: block; font-weight: 400; font-size: 25px; color: var(--sky); letter-spacing: .5px; }

  .band { position: absolute; left: 0; top: 238px; width: 560px; height: 507px; background: var(--band); }

  .card {
    position: absolute; top: 274px; width: 136px; height: 434px;
    background: var(--paper);
  }
  .card__photo { height: 100px; background: linear-gradient(160deg, #d9d4ce 0%, #9e8f82 55%, #5b4f48 100%); }
  .card__body { padding: 14px 12px 0 14px; }
  .card__name { font-size: 12px; font-weight: 500; color: var(--navy); }
  .card__role { font-size: 9.5px; color: var(--navy); margin-top: 1px; line-height: 1.2; }
  .card__bio { font-size: 9px; line-height: 12.6px; color: var(--ink); margin-top: 14px; }

  .footer { position: absolute; left: 0; top: 745px; width: 560px; height: 75px; }
  .folio { position: absolute; top: 24px; font-size: 21px; color: #3a3a3a; }
  .rule { position: absolute; top: 38px; height: 1px; background: #8c8c8c; }
  .contact { position: absolute; top: 28px; font-size: 10px; color: #444; }
  .page--left .folio { left: 72px; }
  .page--left .rule { left: 102px; width: 242px; }
  .page--left .contact { left: 352px; }
  .page--right .folio { right: 68px; }
  .page--right .rule { right: 98px; width: 230px; }
  .contact .sep { margin: 0 4px; color: #888; }
</style>
</head>
<body>
<div class="spread">

  <section class="page page--left">
    <div class="brand">Velmor Dental</div>
    <h1 class="section-title">
      <span class="kicker">OUR SECRET SAUCE</span>
      <span class="sub">THE PEOPLE</span>
    </h1>
    <div class="team-photo" role="img" aria-label="Group photo of the whole team cheering in a bright office"></div>
    <div class="band"></div>

    <article class="card" style="left:75px">
      <div class="card__photo" role="img" aria-label="Portrait of Curt Bellamy"></div>
      <div class="card__body">
        <h2 class="card__name">Curt Bellamy</h2>
        <p class="card__role">Founder &amp; CEO</p>
        <p class="card__bio">Curt Bellamy speaks and consults with dentists all over the world on how to create a Better Practice and a Better Life. As one of Dentistry's Top Seminar Leaders and Online Education Platform Experts, Curt has invested more than 23 years of his professional life optimizing the best systems and practices within the dental industry.</p>
      </div>
    </article>

    <article class="card" style="left:223px">
      <div class="card__photo" role="img" aria-label="Portrait of Lena Ann Fairley"></div>
      <div class="card__body">
        <h2 class="card__name">Lena Ann Fairley</h2>
        <p class="card__role">Director of Coaching</p>
        <p class="card__bio">After becoming a dental hygienist in 2006 Lena Ann was drawn to learning everything possible about what makes dental teams work synergistically, with both effectiveness and efficiency, through collaboration and accountability. Her leadership, facilitation, and coaching skills have been refined through her work with the Harrow Institute and also the Westfield Institute of Cleveland. Being a part of something 'bigger than herself' is a driver in her daily work.</p>
      </div>
    </article>

    <article class="card" style="left:371px">
      <div class="card__photo" role="img" aria-label="Portrait of Beth Jarvis"></div>
      <div class="card__body">
        <h2 class="card__name">Beth Jarvis</h2>
        <p class="card__role">Chief Financial Officer</p>
        <p class="card__bio">Beth Jarvis brings strong organizational and financial skills to the team from her years of experience as a business owner and an independent sales representative. Beth joined us in April 2012, and is the heart of our home office in Kansas City. Beth has a double major in Business Administration with an emphasis in Management and Marketing.</p>
      </div>
    </article>

    <footer class="footer">
      <span class="folio">03</span>
      <span class="rule"></span>
      <span class="contact">800 555 0142<span class="sep">|</span>info@velmordental.com</span>
    </footer>
  </section>

  <section class="page page--right">
    <div class="team-photo" role="img" aria-label="Continuation of the team group photo"></div>
    <div class="brand">Velmor Dental</div>
    <div class="band"></div>

    <article class="card" style="left:65px">
      <div class="card__photo" role="img" aria-label="Portrait of Clara Byers"></div>
      <div class="card__body">
        <h2 class="card__name">Clara Byers</h2>
        <p class="card__role">Lead Practice Coach &amp; Events</p>
        <p class="card__bio">Clara Byers has been involved in dentistry since 1985. Over the years she has held many positions on the dental team including dental assistant, business office, and dental hygienist. Clara's extensive knowledge of the front office and clinical procedures is a great asset and she loves to impart her knowledge to guide dental teams to the best they can achieve a Better Practice Better Life!</p>
      </div>
    </article>

    <article class="card" style="left:213px">
      <div class="card__photo" role="img" aria-label="Portrait of Gina Gorman"></div>
      <div class="card__body">
        <h2 class="card__name">Gina Gorman</h2>
        <p class="card__role">Lead Practice Coach</p>
        <p class="card__bio">Gina Gorman, Lead Coach, brings a breadth of experience gained from her over 25 years serving in the industry. Gina has first hand experience in practice management and patient treatment in general, orthodontic and periodontal offices. She also knows the ownership side from her years owning a periodontal practice. This allows her a unique perspective to better understand the multiple silos in our industry; clinical, leader, manager and owner.</p>
      </div>
    </article>

    <article class="card" style="left:361px">
      <div class="card__photo" role="img" aria-label="Portrait of Sabrina Hollis"></div>
      <div class="card__body">
        <h2 class="card__name">Sabrina Hollis</h2>
        <p class="card__role">Lead Practice Coach</p>
        <p class="card__bio">Sabrina started working in the dental industry when she was just 16 years old. She discovered her deep passion for dentistry early on after developing strong relationships within her team and amongst the amazing patients. She is an absolute expert at all things administrative, and loves the guidance she can provide to all facets of a dental practice. When she is not immersed in her beloved team community, you can find her reading, doing Yoga, kayaking and spending time.</p>
      </div>
    </article>

    <footer class="footer">
      <span class="contact" style="left:65px">800 555 0142<span class="sep">|</span>info@velmordental.com</span>
      <span class="rule"></span>
      <span class="folio">04</span>
    </footer>
  </section>

</div>
</body>
</html>
```